Business Card Design for skin care range

The skincare range created here is a revolutionized skin care range that is very unique, natural and great for all skin types.The skincare range is cooled in nature, organic and rejuvenating for all skin types. 'Glow Tide Bloom' aims to radiate the vibe of wellness and harmony throughout our skin. The products are developed via bio-pharmaceutical high grade processes to put the life and radiance back in our skin.

Target Market(s)

All ages, as the skincare is great for all skin types.

Industry/Entity Type

Business

Contact Information for Business Card

M: 04 587 926 41 E: hello@velqorabeauty.com S: www.velqorabeauty.com

Font styles to use
Serif
Sans Serif
Script

Colors
0692cd

Requirements
Must have
• The business card we are aiming for is a simple yet elegant appeal with a black and white picture set in the middle of the business card (landscape orientation) with the caption "Glow Tide Bloom" centered spanning across the whole card horizontally. We are thinking having coloured (light-ish/ aqua coloured blue). we want the image encapsulated within a prestige/ mirror frame kind of border that is simply shown through the cutting out of the image. The remaining space on the card shall have a white background with a misty tonal fog that sweeps across the white.On the back of the card will be the text "Glow Tide Bloom" in the color blue being the hierarchical text. (same as the 'me' on the front).All other relevant contact information is in black. with also the statement "Keep me chilled" (as the products are to be refrigerated) in a different style so it is unique from the rest as its an important note. Also under the glow tide bloom text, i'd like to have the text "Bio-organic pharmaceutical grade skincare range" added to the card to emphasis the quality and uniqueness of the product. For the back of the card's background, the hazy tonal fog shall span across the whole backside of the card with the white background, keeping it plain and simple.
Nice to have
• Weare aiming for a professional elegant and classy look, with also that natural and joyful appeal.
• A black and white close up picture of a young persons face (preferably a girls face) to create the appeal of youth. The eyes must be of high importance. see the pictures we've uploaded and trial with them as we love the pictures of the girls faces

```html
<!DOCTYPE html>
<html lang="en">
<head>
<meta charset="utf-8">
<title>Glow Tide Bloom – Business Card Design</title>
<link rel="stylesheet" href="https://fonts.googleapis.com/css2?family=Caveat+Brush&family=Pinyon+Script&family=Verdana&family=Open+Sans:wght@400&display=swap">
<style>
  :root {
    --sheet: #ffffff;
    --band-green: #5a8a2a;
    --ink: #111111;
    --accent-pink: #f07fa6;
    --brand-navy: #1f2a72;
    --card-white: #f4f4f4;
    --fog-grey: #d6d6d6;
    --tab-white: #ffffff;
    --photo-dark: #3a3a3a;
    --photo-light: #c9c9c9;
    --deco-aqua: #cfe8ee;
    --deco-lime: #f1f3d6;
    --deco-pink: #f6e3f1;
  }
  * { box-sizing: border-box; margin: 0; padding: 0; }
  html, body { width: 1200px; height: 905px; overflow: hidden; background: var(--sheet); }
  .sheet { position: relative; width: 1200px; height: 905px; overflow: hidden; background: var(--sheet); }
  .band { position: absolute; left: 0; width: 1200px; height: 6px; background: var(--band-green); }
  .band--top { top: 0; }
  .band--bottom { bottom: 0; }
  .sheet-title {
    position: absolute; top: 37px; left: 0; width: 1200px; text-align: center;
    font: 19px "Open Sans", Verdana, sans-serif; color: var(--ink);
  }
  .decor { position: absolute; inset: 0; }

  .card {
    position: absolute; width: 603px; height: 369px; overflow: hidden;
    background:
      radial-gradient(ellipse 60% 40% at 20% 30%, rgba(200,200,200,.45), transparent 70%),
      radial-gradient(ellipse 50% 35% at 85% 75%, rgba(190,190,190,.4), transparent 70%),
      linear-gradient(155deg, transparent 30%, rgba(255,255,255,.8) 45%, transparent 60%),
      linear-gradient(180deg, #ececec, var(--card-white) 50%, #e6e6e6);
    box-shadow: 0 1px 4px rgba(0,0,0,.35);
  }
  .card--front { left: 80px; top: 127px; }
  .card--back { left: 534px; top: 488px; }

  .portrait {
    position: absolute; left: 190px; top: 37px; width: 228px; height: 304px;
    border: 4px solid var(--ink); border-radius: 26px;
    background: radial-gradient(ellipse 60% 55% at 55% 40%, var(--photo-light), var(--photo-dark) 90%);
  }
  .wordmark {
    position: absolute; top: 262px; font-family: "Caveat Brush", cursive;
    font-size: 66px; line-height: 1; color: var(--ink);
  }
  .wordmark--left { right: 430px; }
  .wordmark--mid { left: 304px; transform: translateX(-50%); color: var(--accent-pink); }
  .wordmark--right { left: 432px; }

  .tab {
    position: absolute; top: 18px; width: 258px; height: 33px; background: var(--tab-white);
    font-family: "Pinyon Script", cursive; font-size: 25px; color: var(--ink);
    line-height: 33px; box-shadow: 0 1px 2px rgba(0,0,0,.3);
  }
  .tab--note { left: 0; padding-left: 20px; border-radius: 0 0 6px 0; }
  .tab--phone { right: 0; padding-left: 10px; border-radius: 0 0 0 6px; }
  .brand-name {
    position: absolute; top: 140px; left: 0; width: 100%; text-align: center;
    font-family: "Caveat Brush", cursive; font-size: 74px; line-height: 1; color: var(--brand-navy);
  }
  .tagline {
    position: absolute; top: 225px; left: 0; width: 100%; text-align: center;
    font-family: "Pinyon Script", cursive; font-size: 23px; color: var(--ink);
  }
  .contact {
    position: absolute; top: 318px; font-family: "Pinyon Script", cursive;
    font-size: 25px; color: var(--ink);
  }
  .contact--email { left: 18px; }
  .contact--web { right: 20px; }
</style>
</head>
<body>
<main class="sheet">
  <div class="band band--top"></div>

  <svg class="decor" width="1200" height="905" viewBox="0 0 1200 905" aria-hidden="true">
    <polygon points="222,548 330,548 360,626 330,722 222,722 163,626" fill="var(--deco-aqua)" opacity=".8"/>
    <polygon points="0,785 165,785 190,880 0,880" fill="var(--deco-aqua)" opacity=".6"/>
    <polygon points="320,780 430,775 490,905 360,905" fill="var(--deco-lime)" opacity=".7"/>
    <polygon points="1150,580 1170,580 1170,905 1060,905" fill="var(--deco-pink)" opacity=".6"/>
    <g stroke="var(--deco-pink)" stroke-width="2" opacity=".7">
      <line x1="990" y1="140" x2="1160" y2="420"/>
      <line x1="1015" y1="140" x2="1170" y2="390"/>
      <line x1="1040" y1="140" x2="1170" y2="350"/>
    </g>
  </svg>

  <h1 class="sheet-title">Business Card Design for skin care range</h1>

  <section class="card card--front" aria-label="Card front">
    <div class="portrait" role="img" aria-label="Black and white close-up portrait of a young woman in an ornate mirror frame"></div>
    <span class="wordmark wordmark--left">Glow</span>
    <span class="wordmark wordmark--mid">Tide</span>
    <span class="wordmark wordmark--right">Bloom</span>
  </section>

  <section class="card card--back" aria-label="Card back">
    <div class="tab tab--note">Keep me chilled</div>
    <div class="tab tab--phone">M: 04 587 926 41</div>
    <h2 class="brand-name">Glow Tide Bloom</h2>
    <p class="tagline">Bio-organic pharmaceutical grade skincare range</p>
    <p class="contact contact--email">hello@velqorabeauty.com</p>
    <p class="contact contact--web">www.velqorabeauty.com</p>
  </section>

  <div class="band band--bottom"></div>
</main>
</body>
</html>
```